Summer Drinks Flyer for Coffee Shop

We are a coffee shop in London and would like to have a cool and nice flyer for our summer drinks (juices and frozen drink) flyer - see on the attached file for the list

Attached you can find an "attempt" - please note that I would no necessary need the image below.

I also attache our new logo.

thank you

Industry/Entity Type

Coffee Shop

```html
<!DOCTYPE html>
<html lang="en">
<head>
<meta charset="utf-8">
<title>Soleggia – New Summer Drinks Menu</title>
<link href="https://fonts.googleapis.com/css2?family=Gochi+Hand&family=Questrial&family=Poppins:wght@700&family=Arimo:ital,wght@1,400;1,700&display=swap" rel="stylesheet">
<style>
  :root {
    --gold: #bb872a;
    --gold-dark: #8a5f16;
    --ink: #1d1d1b;
    --white: #ffffff;
    --sun-core: #ffe100;
    --sun-mid: #fff27a;
    --sun-pale: #fffbd6;
    --orange: #f39a1e;
    --drink-red: #e8542a;
    --drink-brown: #9a4a2c;
    --leaf: #7cc242;
  }
  * { margin: 0; padding: 0; box-sizing: border-box; }
  html, body { width: 850px; height: 1200px; overflow: hidden; background: var(--white); }
  .flyer {
    position: relative;
    width: 850px;
    height: 1200px;
    overflow: hidden;
    background: var(--white);
    font-family: "Questrial", sans-serif;
    color: var(--ink);
  }
  .sun-rays {
    position: absolute; inset: 0;
    background: radial-gradient(circle at 86% 74%, var(--sun-core) 0%, var(--sun-core) 14%, var(--sun-mid) 34%, var(--sun-pale) 55%, var(--white) 75%);
  }
  .brand {
    position: absolute; top: 42px; left: 0; width: 850px;
    text-align: center;
    font-size: 36px; letter-spacing: 2px;
    color: var(--gold);
  }
  .brand::before {
    content: ""; display: inline-block;
    width: 16px; height: 16px; border-radius: 50%;
    background: var(--gold); margin-right: 10px; vertical-align: middle;
  }
  .headline {
    position: absolute; top: 138px; left: 0; width: 850px;
    text-align: center;
    font-family: "Gochi Hand", cursive;
    font-size: 108px; line-height: 78px;
    color: var(--gold);
  }
  .menu-col { position: absolute; text-align: center; }
  .col-frozen { left: 20px; width: 240px; top: 344px; }
  .col-juices { left: 290px; width: 280px; top: 344px; }
  .col-iced { left: 600px; width: 240px; top: 344px; }
  .col-title {
    font-family: "Poppins", sans-serif; font-weight: 700;
    font-size: 43px; line-height: 51px;
    color: var(--gold);
  }
  .item { font-size: 28px; line-height: 32px; }
  .divider {
    position: relative; height: 2px; margin: 15px auto;
    background: var(--ink);
  }
  .divider::after {
    content: ""; position: absolute; left: 50%; top: -7px;
    width: 18px; height: 9px; margin-left: -9px;
    border-radius: 9px 9px 0 0; background: var(--gold);
  }
  .col-frozen .divider { width: 200px; }
  .col-juices .divider { width: 280px; }
  .col-iced .divider { width: 178px; }
  .price {
    position: absolute;
    display: flex; align-items: center; justify-content: center; gap: 14px;
    background: var(--gold);
    border-radius: 10px;
    font-family: "Poppins", sans-serif; font-weight: 700;
    font-size: 40px; color: var(--white);
  }
  .price-mark { width: 40px; height: 40px; border-radius: 50%; background: var(--gold-dark); }
  .price-frozen { left: 43px; top: 694px; width: 208px; height: 50px; }
  .price-juices { left: 332px; top: 706px; width: 209px; height: 54px; }
  .price-iced { left: 613px; top: 683px; width: 209px; height: 54px; }
  .note { position: absolute; font-family: "Arimo", sans-serif; font-style: italic; font-size: 19px; text-align: center; }
  .note strong { font-weight: 700; }
  .note-juices { left: 270px; width: 340px; top: 774px; }
  .note-iced { left: 620px; width: 200px; top: 758px; line-height: 25px; }
  .drinks-art {
    position: absolute; left: 34px; top: 812px; width: 560px; height: 345px;
    border-radius: 30px 30px 12px 12px;
    background: linear-gradient(90deg, var(--drink-red) 0%, var(--orange) 30%, var(--drink-brown) 55%, var(--leaf) 85%);
    opacity: 0.85;
  }
  .sun-face-art {
    position: absolute; left: 570px; top: 820px; width: 260px; height: 300px;
    border-radius: 50%;
    background: radial-gradient(circle, var(--sun-core) 0%, #ffd200 70%, var(--sun-mid) 100%);
  }
</style>
</head>
<body>
<main class="flyer">
  <div class="sun-rays" role="img" aria-label="Bright yellow sun rays radiating across the page"></div>

  <div class="brand">soleggia</div>

  <h1 class="headline">New Summer<br>Drinks Menu</h1>

  <section class="menu-col col-frozen">
    <h2 class="col-title">Frozen<br>Fruit<br>Drinks</h2>
    <p class="item">Strawberry<br>&amp; Banana</p>
    <div class="divider"></div>
    <p class="item">Pineapple,<br>Mango &amp;<br>Banana</p>
  </section>

  <section class="menu-col col-juices">
    <h2 class="col-title">Fruit Juices</h2>
    <p class="item">Orange &amp; Carrot</p>
    <div class="divider"></div>
    <p class="item">Orange &amp; Pineapple</p>
    <div class="divider"></div>
    <p class="item">Pineapple &amp; Apple</p>
    <div class="divider"></div>
    <p class="item">Apple &amp; Kiwi</p>
    <div class="divider"></div>
    <p class="item">Carrot &amp; Ginger</p>
  </section>

  <section class="menu-col col-iced">
    <h2 class="col-title">Iced<br>Coffees</h2>
    <p class="item">Iced Coffee</p>
    <div class="divider"></div>
    <p class="item">Iced Latte</p>
    <div class="divider"></div>
    <p class="item">Iced<br>Chocolate<br>Drink</p>
  </section>

  <div class="price price-frozen"><span class="price-mark" role="img" aria-label="Small sun emblem"></span>£2.95</div>
  <div class="price price-juices"><span class="price-mark" role="img" aria-label="Small sun emblem"></span>£2.95</div>
  <div class="price price-iced"><span class="price-mark" role="img" aria-label="Small sun emblem"></span>£2.45</div>

  <p class="note note-juices">Add Mint or Ginger for <strong>FREE!</strong></p>
  <p class="note note-iced">Add Syrup<br>Shot for <strong>10p</strong></p>

  <div class="drinks-art" role="img" aria-label="Illustration of three summer drinks: an orange iced drink with straw and cherry, a chocolate drink in a stemmed glass, and a fruit juice with strawberry, orange slices and mint"></div>
  <div class="sun-face-art" role="img" aria-label="Illustration of a smiling cartoon sun wearing sunglasses"></div>
</main>
</body>
</html>
```